Brochure

I have the brochure content in this file. I would like the photos of the young people on the side, and I can add you to the dropbox folder with their photos. I would like to have the Why we are here as a tagcloud like header for like the sample attached. I would like the phrases why are we here and will you join us in bold on the tag cloud header. Here is my website www.brightpathgathering.info and I would like to use the same color scheme and incorporate the whole globe/world map aspect in someho

Target Market(s)

youth, adults

Requirements
Must have
• it should use the same colors as our site
brightpathgathering.info

```html
<!DOCTYPE html>
<html lang="en">
<head>
<meta charset="utf-8">
<title>Bright Path Gathering – Brochure Inside Spread</title>
<link href="https://fonts.googleapis.com/css2?family=Archivo+Black&family=Arimo:wght@400;700&display=swap" rel="stylesheet">
<style>
:root{
  --page:#e9e4da;
  --panel:#3c3c3c;
  --band:#a9d5f7;
  --band-light:#cfe7fb;
  --fold:#f3f3f3;
  --white:#ffffff;
  --yellow:#f6e21a;
  --gold:#f5a623;
  --sky:#7cc3f2;
}
*{box-sizing:border-box;margin:0;padding:0}
html,body{width:1200px;height:788px;overflow:hidden}
body{background:var(--page);font-family:"Arimo",Arial,sans-serif;color:var(--white)}
.spread{position:absolute;left:42px;top:36px;width:1116px;height:716px;display:flex;background:var(--panel)}
.panel{position:relative;width:372px;height:100%;background:var(--panel);border-right:3px solid var(--fold);overflow:hidden}
.panel:last-child{border-right:none}
.band{height:84px;background:linear-gradient(var(--band) 0 64%,var(--band-light) 64% 100%);position:relative}
.band .num{position:absolute;left:26px;top:2px;font-family:"Archivo Black",Arial,sans-serif;font-size:56px;line-height:1;color:var(--white);text-shadow:2px 2px 0 #6f9ec3}
.band .kicker{position:absolute;left:108px;top:24px;font:700 21px/1 "Arimo",Arial,sans-serif;color:var(--yellow);text-shadow:1px 1px 0 #7a7a2a}
.band .line2{position:absolute;left:38px;top:54px;font:400 24px/1 "Arimo",Arial,sans-serif;color:var(--white)}
.band .kicker.small{font-size:16px;top:30px}
.brand{position:absolute;left:50px;top:4px;width:300px;height:76px;background:var(--white);display:flex;align-items:center;justify-content:center;gap:10px}
.brand-dot{width:26px;height:26px;border-radius:50%;background:#2f8fd6}
.brand-name{font:700 15px/1.15 "Arimo",Arial,sans-serif;color:#1f5f96;text-align:center}
.body{padding:10px 18px 0 18px;font-size:8.4px;line-height:1.22}
.section-title{display:flex;align-items:center;gap:4px;color:var(--yellow);font-size:15px;font-weight:400;margin:10px 0 2px}
.section-title .badge{width:17px;height:17px;border-radius:50%;background:var(--yellow);color:var(--panel);font:700 12px/17px "Arimo",Arial,sans-serif;text-align:center}
.body p{margin-bottom:7px}
.label{color:var(--sky)}
.lead{color:var(--gold);font-weight:700}
.list{list-style:none}
.list li{position:relative;padding-left:10px;margin-bottom:9px}
.list li::before{content:"";position:absolute;left:0;top:2px;width:5px;height:5px;border-radius:50%;background:var(--white)}
.names p{margin:0}
.indent{padding-left:10px}
</style>
</head>
<body>
<main class="spread">

  <section class="panel">
    <header class="band">
      <span class="num">30</span>
      <span class="kicker">Young Leaders</span>
      <span class="line2">from around the World</span>
    </header>
    <div class="body">
      <h2 class="section-title">Section <span class="badge">1</span></h2>
      <div class="indent">
        <p>Message from the Founding Leaders<br>We are excited to demonstrate to the world, our collective effort to not just make an impression, but to make an imprint on practice and policy related to youth in care. This Gathering gives us a real opportunity to work strategically and collaboratively with other stakeholders to ensure that the voices of young people are influencing decisions about the design and daily operation of child welfare systems in every nation and every community, worldwide.</p>
        <div class="names">
          <p>Names and Photos of Founding Leaders</p>
          <p>Planning Committee</p>
          <p class="label">Founding Leaders:</p>
          <p>Dorian Pell, RISE Teens - Washington, DC</p>
          <p>Marisol Kent, RISE Teens - Washington, DC</p>
          <p>Tessa Brandt, RISE Teens - Washington, DC</p>
          <p>Owen Lasker, RISE Teens - Washington, DC</p>
          <p>Jade Corwin, Coastal Youth in Care Alliance</p>
          <p>Nina Varga, Coastal Youth in Care Alliance</p>
          <p>Rosa Whitlow, Northern Youth in Care Circle, Canada</p>
          <p>Ada Fenwick, Northern Youth in Care Circle, Canada</p>
          <p>Colin Ashby, Harbor Light Foundation</p>
          <p>&nbsp;</p>
          <p class="label">Chair</p>
          <p>Renee Holt, RISE Teens, Washington, DC</p>
          <p class="label">Co-Chairs</p>
          <p>Joan Mercer, Global Foster Family Network, Amsterdam, Netherlands</p>
          <p>Leah Danvers, Youth Pathway Partners, Jackson, MS</p>
          <p>Lena Morales, E.C.H.O.E.S., Napa, CA</p>
          <p>Lena Morales, E.C.H.O.E.S., Napa, CA</p>
        </div>
      </div>
      <h2 class="section-title">Section <span class="badge">2</span></h2>
      <p class="indent">Reasons to Attend</p>
      <ul class="list">
        <li>To connect with and be inspired by young activists with personal experience in care and a new generation of leaders from NGOs and government agencies around the globe.</li>
        <li>To develop a deeper understanding of the unique connections between Change and Transition for youth who have been in care.</li>
        <li>To discover, through experiential learning, about the positive value of youth as subject matter experts and not just consumers in the child welfare system.</li>
        <li>To engage young activists, development professionals and policy-makers in discussion together to find new answers and develop new policies around the central Gathering theme, which is transition.</li>
        <li>To promote youth-led development as a constructive and highly cost-effective way to ensure that youth in care are influencing the design and daily operation of care-related policies and practices, worldwide.</li>
        <li>To draw attention of the world—especially those influencing policy—to a</li>
      </ul>
    </div>
  </section>

  <section class="panel">
    <header class="band">
      <span class="num">30</span>
      <span class="kicker small">Stakeholders Influencing</span>
      <span class="line2">Child Welfare Policy</span>
    </header>
    <div class="body">
      <p class="indent">dynamic emerging movement of international youth voice that is leading the charge for improved care systems.</p>
      <ul class="list"><li>To create a positive and unstoppable momentum to making this Gathering a global turning point towards transition awareness and youth-led policy development</li></ul>
      <h2 class="section-title">Section <span class="badge">3</span></h2>
      <p>The Gathering will connect young leaders from across the globe, bringing into existence a social network with enormous potential to challenge, change, and provide solutions for current practices and policies.<br>The Gathering is youth-led and will run from Tuesday, June 26 – arrivals and welcome dinner until Friday, June 29 – Multi-Generational Forum and departures.</p>
      <p class="label">Coming soon: The day-by-day outline of the event.</p>
      <p>Components of the Gathering will include learning labs, world cafes, roundtables, workgroup session, talent showcases, action projects and gallery. Here is a list of some of those main components:</p>
      <p><span class="lead">Gallery and Welcome Center:</span> Both online and at the site, all the delegates and NGOs that attend the Gathering will have the opportunity to exhibit their projects and/or organizational achievements in the Welcome Center. In addition, we will have a gallery showcasing the messages, ideas, sketches, videos, and artwork created by our delegates and other Gathering participants.</p>
      <p><span class="lead">Youth in Care World Congress:</span> 30 invited delegates on-site and hundreds more around the globe will work for three days to share experiences and discuss the challenges they have faced in care and the transitions. Using these shared experiences, they will create the foundation for the first draft of the International Youth in Care Standards for Practices and Policies. We will be linking with other youth in care globally through an online Virtual World Congress.</p>
      <p><span class="lead">Multi-Generational Forum on Transition:</span> This day will begin with an experiential introduction of the Transition Framework developed by Walter Briggs. Our delegates will do a short presentation to share how they connected, learned, and created a roadmap for improving practices and policies. Using world café technology as a tool stakeholders and delegates together will engage in dialogue and the day will close with a pro-action luncheon where those shared ideas and answers become the foundation for the development of The International System Standards for Transition Related Practices and Policies.</p>
      <p><span class="lead">Transition Framework Training:</span> To make the changes we are trying to make happen, successful in lasting, we need to address, first the emotional and psychological impact change and transition have on youth in care. Senior officials and youth alike need to understand the range of emotions people experience as they confront change in their lives. Management consultant Walter Briggs developed the three-point Transition Framework to explain the different phases a person experiences in transition. We will spend a great deal of time during the summit applying this framework as a tool to making the outcomes real action. Understanding that people are resisting the potentially painful process of</p>
    </div>
  </section>

  <section class="panel">
    <header class="band">
      <div class="brand">
        <span class="brand-dot"></span>
        <span class="brand-name">2012 Bright Path Gathering</span>
      </div>
    </header>
    <div class="body">
      <p>transforming themselves in light of the change and not the change itself, can allow social change agents to devise more effective strategies.</p>
      <p><span class="label">Virtual Congress:</span> Many young people who do not have the opportunity to attend the congress in person, will have the chance to listen to and participate in the discussions, pose questions and help draft documents as virtual delegates. Everyone with access to a computer and the internet will be able to connect, via live web streaming.</p>
      <h2 class="section-title">Section <span class="badge">4</span></h2>
      <p>The 2012 Bright Path Gathering is a collaborative event of RISE Teens, ECHOES, Youth Pathway Partners, and Global Foster Family Network. Together we are committed to using this event as a platform for engaging youth in care and the stakeholders that impact their lives while taking the necessary steps to ensure real and positive results.</p>
      <p class="label">GFFN</p>
      <p>The Global Foster Family Network (GFFN) is an international network dedicated solely to the promotion and support of family based foster care across the world. We are a volunteer and member based organisation providing a multi-cultural platform for young people, foster carers, social workers, academics, researchers, volunteers, media, policy makers and others to network and share information on a global basis. GFFN fully supports recent UN legislation stating that all children have the right to a family and our role is to enable the exchange of information through our conferences, consultation and networking to facilitate improvement and promotion of this model within a fostering environment.</p>
      <p class="label">RISE Teen</p>
      <p>Rising Initiatives for Supported Empowerment (RISE) Teens is a non-profit organization led by amazing youth and dedicated staff. Created and led by former foster youth who know all about the flaws in the current system and are determined to make it better for the next generation, the dynamic and committed young leaders of RISE Teens are an inspiration to everyone they meet. Our mission is to empower disadvantaged youth, particularly those in foster care, to become strong self advocates and healthy, self aware young adults who have the resiliency and grit to be successful.</p>
      <p class="label">ECHOES</p>
      <p>ECHOES brings together more than 40 partnering agencies to provide housing, education, employment and wellness services to transitioning youth, ages 16-24. Created and run by former foster youth, ECHOES is the first organization of its kind in the nation.</p>
      <p class="label">Youth Pathway Partners</p>
      <p>Youth Pathway Partners LLC (YPP), created by an alumna of the foster care and mental health systems, helps youth and adults develop the skills necessary to create positive outcomes for youth and youth serving organizations.</p>
    </div>
  </section>

</main>
</body>
</html>
```